Brookmere Osteopathy flyer

I want a clean clear DL flyer (but also want an A4 poster) promoting a new Osteopathic business in a semi rural area in Tasmania (Australia).
It can have pictures like the examples attached to show people what Osteopathy is (its like Chiropractic and physiotherapy).
I am the sole practioner and am male, so any pictures would be best to be a white male if possible.
I've attached some wording, you can use all, or none of it
I don't have a phone number for the business yet
info@brookmereosteopathy.example
www.brookmereosteopathy.example
Target Market(s)
Australians, from tradies, professionals, babies to retired people
Industry/Entity Type
Health
Look and feel

```html
<!DOCTYPE html>
<html lang="en">
<head>
<meta charset="utf-8">
<title>Brookmere Osteopathy – DL Flyer</title>
<link href="https://fonts.googleapis.com/css2?family=Montserrat:wght@500;600;700&family=Poppins:wght@800&family=Barlow:wght@500;600&display=swap" rel="stylesheet">
<style>
  :root{
    --blue:#0f95d3;
    --orange:#f5901e;
    --ink:#111111;
    --white:#ffffff;
    --stage:#e9eaec;
    --photo-skin:#e6c3a5;
    --photo-cool:#c9d3dc;
  }
  *{margin:0;padding:0;box-sizing:border-box}
  html,body{width:1200px;height:1183px;overflow:hidden;background:var(--stage)}
  .canvas{position:relative;width:1200px;height:1183px}
  .panel{position:absolute;top:130px;width:435px;height:923px;background:var(--white);overflow:hidden;box-shadow:0 4px 14px rgba(0,0,0,.18)}
  .panel--front{left:132px}
  .panel--back{left:634px}
  .panel svg.shapes{position:absolute;left:0;top:0;width:435px;height:923px}
  .t{position:absolute;left:0;width:100%;text-align:center}

  .brand{position:absolute;left:145px;top:40px;width:145px;height:145px;border:2px solid var(--blue);border-radius:50%;display:flex;align-items:center;justify-content:center;text-align:center;font-family:'Montserrat',sans-serif;font-weight:600;font-size:15px;line-height:1.25;color:var(--blue)}
  .headline{font-family:'Montserrat',sans-serif;font-weight:700;line-height:1;letter-spacing:.5px}
  .headline--blue{color:var(--blue);font-size:37px}
  .headline--black{color:var(--ink);font-size:37px}
  .headline--orange{color:var(--orange);font-size:54px}
  .touch{font-family:'Montserrat',sans-serif;font-weight:600;font-size:17px;color:var(--white)}
  .contact{font-family:'Poppins',sans-serif;font-weight:800;font-size:46px;color:var(--ink);line-height:1}
  .rule{position:absolute;left:190px;top:805px;width:55px;height:3px;background:var(--orange)}
  .link{font-family:'Montserrat',sans-serif;font-weight:500;font-size:17px;color:var(--white)}

  .conditions{position:absolute;left:48px;top:34px;list-style:none;font-family:'Barlow',sans-serif;font-weight:600;font-size:18.5px;color:var(--white)}
  .conditions li{height:31px;line-height:31px;padding-left:14px;position:relative}
  .conditions li::before{content:"";position:absolute;left:0;top:14px;width:4px;height:4px;border-radius:50%;background:var(--white)}
  .about-title{font-family:'Montserrat',sans-serif;font-weight:700;font-size:19px;color:var(--blue)}
  .about-text{font-family:'Montserrat',sans-serif;font-weight:500;font-size:12.6px;line-height:17px;color:var(--ink);padding:0 46px}
  .call{position:absolute;left:129px;top:810px}
  .call-label{font-family:'Montserrat',sans-serif;font-weight:700;font-size:19px;color:var(--orange);line-height:1}
  .call-number{font-family:'Montserrat',sans-serif;font-weight:700;font-size:31px;color:var(--ink);line-height:1.1}
  .phone-icon{position:absolute;left:68px;top:814px;width:48px;height:48px}
</style>
</head>
<body>
<div class="canvas">

  <section class="panel panel--front">
    <svg class="shapes" viewBox="0 0 701 1487" preserveAspectRatio="none">
      <polygon points="0,925 100,858 130,885 0,958" fill="var(--orange)"/>
      <polygon points="701,925 601,858 571,885 701,958" fill="var(--orange)"/>
      <polygon points="0,958 130,885 350,780 571,885 701,958 701,1487 0,1487" fill="var(--blue)"/>
      <g transform="rotate(45 353 886)"><rect x="172" y="705" width="362" height="362" rx="40" fill="var(--white)"/></g>
      <g role="img" aria-label="Osteopath's hands treating a patient's back" transform="rotate(45 353 886)"><rect x="186" y="719" width="334" height="334" rx="32" fill="var(--photo-skin)"/></g>
      <g transform="rotate(45 493 761)"><rect x="398" y="666" width="190" height="190" rx="28" fill="var(--white)"/></g>
      <g role="img" aria-label="Hands massaging a patient's upper back" transform="rotate(45 493 761)"><rect x="410" y="678" width="166" height="166" rx="22" fill="#efd2ba"/></g>
      <g transform="rotate(45 500 1031)"><rect x="402" y="933" width="196" height="196" rx="28" fill="var(--white)"/></g>
      <g role="img" aria-label="Patient receiving gentle head and neck treatment" transform="rotate(45 500 1031)"><rect x="414" y="945" width="172" height="172" rx="22" fill="var(--photo-cool)"/></g>
    </svg>

    <div class="brand">Brookmere<br>Osteopathy</div>

    <div class="t headline headline--blue" style="top:197px">COMMON</div>
    <div class="t headline headline--blue" style="top:240px">REASONS PEOPLE</div>
    <div class="t headline headline--black" style="top:283px">VISIT AN</div>
    <div class="t headline headline--orange" style="top:327px">OSTEOPATH</div>

    <div class="t touch" style="top:726px">Get in touch</div>
    <div class="t contact" style="top:749px">Contact</div>
    <div class="rule"></div>
    <div class="t link" style="top:822px">www.brookmereosteopathy.example</div>
    <div class="t link" style="top:851px">info@brookmereosteopathy.example</div>
  </section>

  <section class="panel panel--back">
    <svg class="shapes" viewBox="0 0 701 1487" preserveAspectRatio="none">
      <path d="M0 0 H701 V901 L395 586 Q373 563 351 586 L0 901 Z" fill="var(--blue)"/>
      <g transform="rotate(45 350 724)"><rect x="261" y="635" width="178" height="178" rx="34" fill="var(--orange)"/></g>
      <g role="img" aria-label="Hands supporting a pregnant patient's belly" transform="rotate(45 350 724)"><rect x="275" y="649" width="150" height="150" rx="26" fill="var(--photo-skin)"/></g>
      <g transform="rotate(45 205 892)"><rect x="116" y="803" width="178" height="178" rx="34" fill="var(--orange)"/></g>
      <g role="img" aria-label="Woman relaxing on a treatment table during a session" transform="rotate(45 205 892)"><rect x="130" y="817" width="150" height="150" rx="26" fill="var(--photo-cool)"/></g>
      <g transform="rotate(45 497 892)"><rect x="408" y="803" width="178" height="178" rx="34" fill="var(--orange)"/></g>
      <g role="img" aria-label="Baby receiving gentle cranial osteopathy" transform="rotate(45 497 892)"><rect x="422" y="817" width="150" height="150" rx="26" fill="#a9c6e2"/></g>
      <line x1="167" y1="1090" x2="335" y2="1090" stroke="var(--orange)" stroke-width="2"/>
      <line x1="365" y1="1090" x2="534" y2="1090" stroke="var(--orange)" stroke-width="2"/>
      <polygon points="350,1082 358,1090 350,1098 342,1090" fill="var(--blue)"/>
    </svg>

    <ul class="conditions">
      <li>Back / neck pain</li>
      <li>Headaches / migraines</li>
      <li>Joint and muscle pain</li>
      <li>Pregnancy-related discomfort</li>
      <li>Disc related issues</li>
      <li>Sciatica</li>
      <li>Plantar fasciitis</li>
      <li>Tendonitis / Bursitis</li>
      <li>Adhesive capsulitis (frozen shoulder)</li>
      <li>Tennis / Golfers elbow</li>
    </ul>

    <div class="t about-title" style="top:641px">ABOUT US</div>
    <p class="t about-text" style="top:692px">Osteopaths use a combination of joint manipulation, targeted deep tissue massage and stretching to improve function, relieve pain and support the body’s ability to heal itself.</p>

    <svg class="phone-icon" viewBox="0 0 48 48" aria-hidden="true">
      <path d="M10 6c2-1 4-1 5 1l4 7c1 2 0 3-1 4l-3 2c2 5 6 9 11 11l2-3c1-1 2-2 4-1l7 4c2 1 2 3 1 5l-3 4c-2 2-5 3-9 1C17 37 9 29 5 18c-1-4 0-7 2-9z" fill="var(--blue)"/>
      <path d="M27 13a9 9 0 0 1 8 8M28 7a15 15 0 0 1 13 13M29 1a21 21 0 0 1 18 18" fill="none" stroke="var(--blue)" stroke-width="2.5" stroke-linecap="round"/>
    </svg>
    <div class="call">
      <div class="call-label">CALL TODAY :</div>
      <div class="call-number">(000) 123-4567</div>
    </div>
  </section>

</div>
</body>
</html>
```